NEED A BUSINESS CARD FOR A NEW ELECTRICAL BUSINESS

HI I am after a new business card for my new electrical business I have a logo that I have attached its the one in blue, I would like that on the front and on the back my name- Leonard Pike, Email leonardpike@tallmesh.com, mobile 0491362047, licence no# vic 47819, nsw 591304k I wont something that is a stand out from the rest but at the same time is neat as being a new business I wont it to catch peoples eye on the front of the card I would like the logo and not much else.
And on the back as well I would like a slogan saying something like
Quality-Reliable-Service

Hi all on the back of the card I would like a little slogan like Quality-Reliable-Service something like that would be good thanks

Hi all the business card needs to have both these licence numbers on it                                                  VIC-47819 nsw-591304k

```html
<!DOCTYPE html>
<html lang="en">
<head>
<meta charset="utf-8">
<title>Leonard Pike Electrical – Business Card</title>
<link href="https://fonts.googleapis.com/css2?family=Exo+2:wght@400;500;600&display=swap" rel="stylesheet">
<style>
  :root {
    --stage: #5a5a5a;
    --card: #050508;
    --band: #1596cc;
    --ink: #ffffff;
    --brand: #1e88d6;
  }
  * { box-sizing: border-box; margin: 0; padding: 0; }
  html, body {
    width: 1200px; height: 903px; overflow: hidden;
    background: var(--stage);
    font-family: "Exo 2", sans-serif;
    color: var(--ink);
  }
  .canvas { position: relative; width: 1200px; height: 903px; }
  .card {
    position: absolute; left: 250px;
    width: 700px; height: 400px;
    background: var(--card);
    box-shadow: 0 12px 30px rgba(0,0,0,.45);
    overflow: hidden;
  }
  .card--back { top: 36px; }
  .card--front { top: 467px; }

  /* back */
  .slogan-band {
    position: absolute; left: 0; right: 0; top: 150px; height: 92px;
    background: var(--band);
    display: flex; align-items: center; justify-content: flex-end;
    padding-right: 48px; gap: 14px;
  }
  .slogan-band__text { font-size: 26px; font-weight: 500; letter-spacing: .5px; margin-right: 10px; }
  .slogan-band__dot { width: 24px; height: 24px; border-radius: 50%; background: var(--ink); }

  /* front */
  .holder { position: absolute; left: 70px; top: 44px; }
  .holder__name { font-size: 34px; font-weight: 500; letter-spacing: 1px; }
  .holder__role { font-size: 19px; font-weight: 500; letter-spacing: 1px; margin-left: -14px; margin-top: 2px; }

  .contact { position: absolute; left: 0; top: 132px; width: 420px; }
  .contact__row {
    position: relative;
    padding: 12px 0 12px 60px;
    border-bottom: 2px solid var(--ink);
    font-size: 17px; letter-spacing: .8px; line-height: 1.45;
  }
  .contact__row:nth-child(1) { margin-left: 50px; }
  .contact__row:nth-child(2) { margin-left: 38px; }
  .contact__row:nth-child(3) { margin-left: 26px; }
  .contact__icon { position: absolute; left: 20px; top: 50%; transform: translateY(-50%); width: 24px; height: 24px; }

  .brand {
    position: absolute; left: 470px; top: 150px; width: 210px;
    display: flex; align-items: center; gap: 10px;
  }
  .brand__square { width: 34px; height: 34px; background: var(--brand); flex: none; }
  .brand__name { font-size: 17px; font-weight: 600; color: var(--brand); letter-spacing: 1px; line-height: 1.2; }
</style>
</head>
<body>
<main class="canvas">
  <section class="card card--back" aria-label="Card back">
    <div class="slogan-band">
      <span class="slogan-band__text">Quality-Reliable-Service</span>
      <span class="slogan-band__dot"></span>
      <span class="slogan-band__dot"></span>
      <span class="slogan-band__dot"></span>
      <span class="slogan-band__dot"></span>
    </div>
  </section>

  <section class="card card--front" aria-label="Card front">
    <div class="holder">
      <h1 class="holder__name">LEONARD PIKE</h1>
      <p class="holder__role">FOUNDER</p>
    </div>

    <div class="contact">
      <div class="contact__row">
        <svg class="contact__icon" viewBox="0 0 24 24" fill="#fff"><path d="M6.6 2.5c.6-.3 1.3 0 1.6.6l1.5 3.4c.2.5.1 1.1-.3 1.4L8 9c.9 2.5 2.6 4.6 4.9 6l1.3-1.3c.4-.4 1-.5 1.5-.2l3.3 1.7c.6.3.8 1 .5 1.6l-1 2.1c-.4.8-1.3 1.2-2.2 1C9.4 18.4 4.5 12.7 4.3 5.6c0-.9.5-1.7 1.3-2.1z"/></svg>
        <span>0491362047<br>Licence VIC-47819</span>
      </div>
      <div class="contact__row">
        <svg class="contact__icon" viewBox="0 0 24 24" fill="#fff"><path d="M12 2a7 7 0 0 0-7 7c0 5 7 13 7 13s7-8 7-13a7 7 0 0 0-7-7zm0 9.5A2.5 2.5 0 1 1 12 6.5a2.5 2.5 0 0 1 0 5z"/></svg>
        <span>Licence NSW-591304k</span>
      </div>
      <div class="contact__row">
        <svg class="contact__icon" viewBox="0 0 24 24" fill="none" stroke="#fff" stroke-width="2"><rect x="3" y="4" width="18" height="12"/><path d="M8 20h8M12 16v4"/></svg>
        <span>leonardpike@tallmesh.com<br>www.leonardpike-electrical.com</span>
      </div>
    </div>

    <div class="brand">
      <span class="brand__square"></span>
      <span class="brand__name">LEONARD PIKE ELECTRICAL</span>
    </div>
  </section>
</main>
</body>
</html>
```